WordPress website in children books redesign

We are personalised children storybook creators with a range of personalized books, music CDs and DVDs that are created for each child. We sell our concept through a license via distributors / entrepreneurs mainly based in France and Europe. We want to focus on selling B2C to parents and grandparents, looking to buy presents to their children aged 0 to 10 years old. Those present are educative, unique for each child, and they will learn to have fun and learn to have fun. I would like to redesign our WordPress website https://pebblelanternkids.co.uk/index.php We are a children in the world of books and music books: books, music CDs and DVDs looking for something a little more along the lines of our competitors. See ike www.quillotop.com, www.tavirosa.com, www.lecheminduvelours.com, https://www.lespetitsbrume.com/, https://tinselpaths.com/ Our current website is a bit too old fashioned so I am looking at a much more modern design Here is a link for a few products that are not available here: https://www.filecrate.example/sh/kq417dzopfrnwtb/BXPL3rYmOk2u-sVH4dQkLN-zb?dl=0 We have 2 sides in our website: B2C on the left side and B2B on the right site; B2B is for distributors that are entrepreneurs buying our concept. for the homepage design, the main focus will be B2Consumer Our current page is too blended, lacks reassurance elements and I would like to have a look at this page. from our current stories. here is a link for our business book to give you a feel for it: http://online.pagewavo.com/qtlk/pzme/ MAIN PAGES TO REVIEW / HOMEPAGE / https://pebblelanternkids.co.uk/ BOOKS: https : //pebblelanternkids.co.uk/product-category/personalised-books/ MUSIC: https://pebblelanternkids.co.uk/product-category/music-cds/ BLOG: https://pebblelanternkids.co.uk/blog -2 / Looking forward to seeing you and your questions asap

Target Market(s)

parents and grandparents of children aged 0 to 10 years old. This is for the European market

Industry/Entity Type

Publishing Company

Number of Pages Required

4 page

Colors
0392cd
9bcb3b
ec1f27
757575

Requirements
Must have
• keep within the color code of our RGB logo: D25028 RGB: 8CC364 329BC8 808285
Nice to have
• be more with the style of our competitors. Pebble Lantern Kids am about making children learn the fun way, and develop their morality, self-esteem and confidence. It's about the magic of reading to help children learn while having fun. I have attached visuals but those are just examples and you we encourage you to suggest other ideas

```html
<!DOCTYPE html>
<html lang="en">
<head>
<meta charset="utf-8">
<title>Pebble Lantern Kids — Personalised Books</title>
<link rel="stylesheet" href="https://fonts.googleapis.com/css2?family=Nunito:wght@400;600;700;800&display=swap">
<style>
  :root {
    --blue: #0392cd;
    --green: #9bcb3b;
    --red: #ec1f27;
    --grey: #757575;
    --orange: #d25028;
    --yellow: #f6c530;
    --ink: #4a4a4a;
    --page: #e4f1f8;
    --footer: #3aa3d6;
    --white: #ffffff;
  }
  * { box-sizing: border-box; margin: 0; padding: 0; }
  html, body { width: 1200px; height: 2284px; overflow: hidden; }
  body {
    position: relative;
    background: var(--page);
    font-family: "Nunito", sans-serif;
    color: var(--ink);
  }
  .abs { position: absolute; }

  /* Hero */
  .hero {
    left: 0; top: 0; width: 1200px; height: 236px;
    background: linear-gradient(180deg, #1b3f7a 0%, #2f6fb3 55%, #9fd0ee 100%);
  }
  .brand {
    left: 480px; top: 14px; width: 240px; height: 200px;
    display: flex; flex-direction: column; align-items: center; justify-content: center; gap: 12px;
  }
  .brand-dot { width: 120px; height: 120px; border-radius: 50%; background: var(--white); }
  .brand-name { font-weight: 800; font-size: 28px; color: var(--white); text-align: center; line-height: 1.1; }
  .cart {
    left: 1060px; top: 130px; width: 72px; height: 72px;
    border-radius: 10px; background: var(--white);
    display: flex; align-items: center; justify-content: center;
  }

  /* Navigation */
  .nav {
    left: 20px; top: 236px; width: 1160px; height: 36px;
    display: flex; justify-content: space-between; align-items: center;
    font-size: 20px; font-weight: 600; color: var(--grey); letter-spacing: 0.5px;
  }
  .nav-right { display: flex; gap: 14px; }

  /* Product circles */
  .product {
    width: 180px; height: 180px; border-radius: 50%;
    background: var(--white);
    border: 10px solid var(--red);
    box-shadow: 0 0 0 8px var(--green), 0 0 0 14px var(--white);
    display: flex; flex-direction: column; align-items: center; justify-content: center;
    text-align: center; font-weight: 700; font-size: 30px; line-height: 1;
  }
  .product--music { left: 250px; top: 320px; color: var(--blue); }
  .product--books { left: 510px; top: 320px; color: var(--green); }
  .product--dvd { left: 820px; top: 320px; color: var(--orange); }
  .product svg { margin-top: 8px; }

  /* Text panels */
  .panel { font-size: 28px; line-height: 34px; }
  .panel svg { position: absolute; left: 0; top: 0; }
  .panel-text { position: absolute; left: 56px; top: 26px; right: 40px; }
  .panel-text p + p { margin-top: 22px; }
  .panel--intro { left: 120px; top: 600px; width: 960px; height: 230px; }
  .panel--why { left: 120px; top: 1030px; width: 960px; height: 352px; }
  .panel--story { left: 120px; top: 1594px; width: 960px; height: 290px; }

  /* Child portraits */
  .ribbon { height: 44px; border-radius: 6px; }
  .ribbon--a { left: 290px; top: 900px; width: 160px; background: var(--blue); }
  .ribbon--b { left: 520px; top: 900px; width: 160px; background: var(--green); }
  .ribbon--c { left: 745px; top: 900px; width: 160px; background: var(--red); }
  .portrait {
    width: 116px; height: 116px; border-radius: 50%;
    border: 6px solid var(--white);
    background: linear-gradient(160deg, #f1d6b8, #b6c9d9);
  }
  .portrait--a { left: 312px; top: 862px; }
  .portrait--b { left: 542px; top: 862px; }
  .portrait--c { left: 767px; top: 862px; }

  /* Illustration bands */
  .band-fairy {
    left: 0; top: 1386px; width: 1200px; height: 196px;
    background: linear-gradient(90deg, #7cc4e8 0%, #f3d36a 35%, #f09ab8 60%, #9fd2f2 100%);
  }
  .band-kids {
    left: 0; top: 1892px; width: 1200px; height: 150px;
    background: linear-gradient(180deg, #cfe8f7 0%, #f2e2b8 100%);
  }

  /* Footer */
  .footer {
    left: 0; top: 2042px; width: 1200px; height: 242px;
    background: var(--footer); color: var(--white);
  }
  .footer-col { position: absolute; top: 34px; font-size: 17px; line-height: 27px; font-weight: 600; }
  .footer-col h3 { font-size: 17px; font-weight: 700; }
  .footer-col ul { list-style: none; padding-left: 30px; }
  .footer-col--collections { left: 96px; }
  .footer-col--packs { left: 510px; }
  .footer-col--packs ul, .footer-col--info ul { padding-left: 0; }
  .footer-col--info { left: 860px; }
</style>
</head>
<body>

<header class="abs hero" role="img" aria-label="Illustrated space adventure scene with children in a rocket among stars"></header>
<div class="abs brand">
  <div class="brand-dot"></div>
  <div class="brand-name">Pebble Lantern Kids</div>
</div>
<div class="abs cart" aria-label="Basket">
  <svg width="44" height="40" viewBox="0 0 44 40"><path d="M2 4h7l5 22h22l5-16H12" fill="none" stroke="#757575" stroke-width="3.5" stroke-linejoin="round"/><circle cx="17" cy="34" r="3.5" fill="#757575"/><circle cx="33" cy="34" r="3.5" fill="#757575"/></svg>
</div>

<nav class="abs nav">
  <span>OUR PRODUCTS</span>
  <span class="nav-right"><span>FOR DISTRIBUTORS</span><span>BLOG</span><span>CONTACT</span></span>
</nav>

<a class="abs product product--music">Music CDs
  <svg width="60" height="50" viewBox="0 0 60 50"><path d="M14 40V10l32-6v30" fill="none" stroke="#0392cd" stroke-width="4"/><circle cx="9" cy="40" r="7" fill="#ec1f27"/><circle cx="41" cy="34" r="7" fill="#9bcb3b"/></svg>
</a>
<a class="abs product product--books">All Books
  <svg width="70" height="46" viewBox="0 0 70 46"><path d="M35 8C25 2 12 2 4 6v36c8-4 21-4 31 2 10-6 23-6 31-2V6c-8-4-21-4-31 2z" fill="none" stroke="#0392cd" stroke-width="4"/><path d="M35 8v36" stroke="#0392cd" stroke-width="4"/></svg>
</a>
<a class="abs product product--dvd">DVD
  <svg width="70" height="50" viewBox="0 0 70 50"><rect x="4" y="4" width="62" height="38" rx="4" fill="#0392cd"/><rect x="10" y="10" width="50" height="26" fill="#9bcb3b"/><rect x="26" y="42" width="18" height="6" fill="#757575"/></svg>
</a>

<section class="abs panel panel--intro">
  <svg width="960" height="230" viewBox="0 0 960 230">
    <rect x="3" y="3" width="954" height="224" rx="28" fill="none" stroke="#ec1f27" stroke-width="4" stroke-dasharray="16 48"/>
    <rect x="3" y="3" width="954" height="224" rx="28" fill="none" stroke="#0392cd" stroke-width="4" stroke-dasharray="16 48" stroke-dashoffset="16"/>
    <rect x="3" y="3" width="954" height="224" rx="28" fill="none" stroke="#9bcb3b" stroke-width="4" stroke-dasharray="16 48" stroke-dashoffset="32"/>
    <rect x="3" y="3" width="954" height="224" rx="28" fill="none" stroke="#f6c530" stroke-width="4" stroke-dasharray="16 48" stroke-dashoffset="48"/>
  </svg>
  <div class="panel-text">
    <p>Is to make children the heroes of the adventure and live magical and unforgettable moments they can share with their family and friends.</p>
    <p>Scenarios are adapted to every age, imagined and conceived in association with children, schools, speech therapists, psychologists and childhood experts.</p>
  </div>
</section>

<div class="abs ribbon ribbon--a"></div>
<div class="abs ribbon ribbon--b"></div>
<div class="abs ribbon ribbon--c"></div>
<div class="abs portrait portrait--a" role="img" aria-label="Photo of a child reading a personalised book"></div>
<div class="abs portrait portrait--b" role="img" aria-label="Photo of a child enjoying a story"></div>
<div class="abs portrait portrait--c" role="img" aria-label="Photo of a child with a storybook"></div>

<section class="abs panel panel--why">
  <svg width="960" height="352" viewBox="0 0 960 352">
    <rect x="3" y="3" width="954" height="346" rx="28" fill="none" stroke="#ec1f27" stroke-width="4" stroke-dasharray="16 48"/>
    <rect x="3" y="3" width="954" height="346" rx="28" fill="none" stroke="#0392cd" stroke-width="4" stroke-dasharray="16 48" stroke-dashoffset="16"/>
    <rect x="3" y="3" width="954" height="346" rx="28" fill="none" stroke="#9bcb3b" stroke-width="4" stroke-dasharray="16 48" stroke-dashoffset="32"/>
    <rect x="3" y="3" width="954" height="346" rx="28" fill="none" stroke="#f6c530" stroke-width="4" stroke-dasharray="16 48" stroke-dashoffset="48"/>
  </svg>
  <div class="panel-text">
    <p>Personalisation offers for children to have an opportunity to recognise themselves in the story, thus developing the morale, self-esteem and confidence. All our stories aim to stimulate learning and enhance reading passion from an early age and have been designed with high-quality original artwork with bright colours to fully engage a child's imagination. The stories are written in an educational and informative way, whilst remaining fun, positive, and engaging.</p>
  </div>
</section>

<div class="abs band-fairy" role="img" aria-label="Illustrated fairy tale characters in a colourful meadow"></div>

<section class="abs panel panel--story">
  <svg width="960" height="290" viewBox="0 0 960 290">
    <rect x="3" y="3" width="954" height="284" rx="28" fill="none" stroke="#ec1f27" stroke-width="4" stroke-dasharray="16 48"/>
    <rect x="3" y="3" width="954" height="284" rx="28" fill="none" stroke="#0392cd" stroke-width="4" stroke-dasharray="16 48" stroke-dashoffset="16"/>
    <rect x="3" y="3" width="954" height="284" rx="28" fill="none" stroke="#9bcb3b" stroke-width="4" stroke-dasharray="16 48" stroke-dashoffset="32"/>
    <rect x="3" y="3" width="954" height="284" rx="28" fill="none" stroke="#f6c530" stroke-width="4" stroke-dasharray="16 48" stroke-dashoffset="48"/>
  </svg>
  <div class="panel-text">
    <p>Pebble Lantern Kids has created and developed a unique concept that allows you to prepare and sell high quality award-winning personalised children books in few minutes only.<br>In each story, the children become the heroes of the adventure and lives magical and unforgettable moments they can share with their family and friends.</p>
  </div>
</section>

<div class="abs band-kids" role="img" aria-label="Illustrated story characters and children waving"></div>

<footer class="abs footer">
  <div class="footer-col footer-col--collections">
    <h3>Our collections</h3>
    <ul>
      <li>Personalised books</li>
      <li>Personalised music albums</li>
      <li>Personalised DVD cartoon</li>
      <li>Personalised school books</li>
    </ul>
  </div>
  <div class="footer-col footer-col--packs">
    <ul>
      <li>Discovery pack</li>
      <li>&nbsp;</li>
      <li>Gold pack</li>
      <li>&nbsp;</li>
      <li>Platinum pack</li>
      <li>&nbsp;</li>
      <li>Bedtime stories</li>
    </ul>
  </div>
  <div class="footer-col footer-col--info">
    <ul>
      <li>Order samples</li>
      <li>&nbsp;</li>
      <li>About Us</li>
      <li>&nbsp;</li>
      <li>Contact Us</li>
      <li>&nbsp;</li>
      <li>Recruitment</li>
    </ul>
  </div>
</footer>

</body>
</html>
```